BrightKeel Business Card Contest

We are looking for a modern business card that catches attention and is unique. Attached is the brand guide and logo files. Please note that the back side (not the side with our name and info) with be UV raise printed, so have fun with the design there. We want to include Name, Title, Phone number, email, website.

Contact Information for Business Card

Please see project description

```html
<!DOCTYPE html>
<html lang="en">
<head>
<meta charset="utf-8">
<title>BrightKeel Business Card</title>
<link rel="stylesheet" href="https://fonts.googleapis.com/css2?family=Outfit:wght@400;500&display=swap">
<style>
  :root {
    --bg: #e6e6e6;
    --ink: #16161a;
    --panel-dark: #202127;
    --paper: #ffffff;
    --light: #f2f2f2;
    --accent-orange: #ef7d22;
    --accent-red: #e0412b;
    --accent-sky: #5fc3ea;
    --accent-blue: #1d5bb8;
    --photo-warm: #b88a64;
    --photo-deep: #5a4638;
  }
  * { margin: 0; padding: 0; box-sizing: border-box; }
  html, body {
    width: 1200px; height: 1200px; overflow: hidden;
    background: var(--bg);
    font-family: "Outfit", sans-serif;
    color: var(--ink);
  }
  .card {
    position: absolute;
    left: 183px;
    width: 834px;
    height: 477px;
    overflow: hidden;
  }
  .card--front { top: 62px; background: var(--panel-dark); }
  .card--back { top: 638px; background: var(--paper); }

  .corner-mark {
    position: absolute; right: 0; bottom: 0;
    width: 11px; height: 11px; background: var(--panel-dark);
  }

  /* Front */
  .front-brand {
    position: absolute; left: 0; top: 0; width: 419px; height: 100%;
  }
  .front-brand__name {
    position: absolute; left: 0; width: 100%; top: 254px;
    text-align: center; font-size: 52px; font-weight: 500;
    line-height: 1; color: var(--light); letter-spacing: -0.5px;
  }
  .front-brand__mark {
    position: absolute; left: 185px; top: 160px;
    width: 48px; height: 48px; background: var(--accent-sky);
  }
  .front-brand__web {
    position: absolute; left: 30px; top: 433px;
    font-size: 18px; line-height: 1; color: var(--light);
  }
  .front-brand__web span { color: var(--accent-orange); }
  .front-photo {
    position: absolute; left: 419px; top: 0; right: 0; height: 100%;
    background: linear-gradient(160deg, #8d7c6a 0%, var(--photo-warm) 35%, #c9a27a 55%, var(--photo-deep) 100%);
  }

  /* Back */
  .back-logo {
    position: absolute; left: 46px; top: 43px;
    display: flex; align-items: center; gap: 6px;
    font-size: 22px; font-weight: 500; line-height: 1;
  }
  .back-logo__mark { width: 18px; height: 18px; background: var(--accent-blue); }
  .person__name {
    position: absolute; left: 46px; top: 205px;
    font-size: 38px; font-weight: 500; line-height: 1; letter-spacing: -0.3px;
  }
  .person__title {
    position: absolute; left: 46px; top: 250px;
    font-size: 19px; font-weight: 500; line-height: 1;
  }
  .contact-rule {
    position: absolute; left: 466px; top: 210px;
    width: 2px; height: 221px;
    background: linear-gradient(to bottom, var(--accent-red), var(--accent-orange) 35%, var(--accent-sky) 75%, var(--accent-blue));
  }
  .contact-item { position: absolute; left: 491px; line-height: 1; }
  .contact-item__label { position: absolute; left: 0; font-size: 11px; }
  .contact-item__value { position: absolute; left: 0; white-space: nowrap; font-weight: 500; }
  .contact-item--address .contact-item__value { font-size: 16px; line-height: 20px; }
  .contact-item--line .contact-item__value { font-size: 19px; }
</style>
</head>
<body>
  <section class="card card--front">
    <div class="front-brand">
      <div class="front-brand__mark"></div>
      <div class="front-brand__name">BrightKeel</div>
      <div class="front-brand__web">www.brightkeel<span>.com</span></div>
    </div>
    <div class="front-photo" role="img" aria-label="Photo of two colleagues at a table, one holding a phone and one writing in a notebook, with shelves behind"></div>
    <div class="corner-mark"></div>
  </section>

  <section class="card card--back">
    <div class="back-logo"><span class="back-logo__mark"></span>BrightKeel</div>
    <div class="person__name">Thomas Harlow</div>
    <div class="person__title">Managing Director</div>
    <div class="contact-rule"></div>

    <div class="contact-item contact-item--address" style="top:211px">
      <span class="contact-item__label" style="top:0">01</span>
      <span class="contact-item__value" style="top:15px">42 Larkfield Street, Manchester<br>M3 7QP, United Kingdom</span>
    </div>
    <div class="contact-item contact-item--line" style="top:287px">
      <span class="contact-item__label" style="top:0">02</span>
      <span class="contact-item__value" style="top:19px">+44 7700 900456</span>
    </div>
    <div class="contact-item contact-item--line" style="top:339px">
      <span class="contact-item__label" style="top:0">03</span>
      <span class="contact-item__value" style="top:18px">thomas.harlow@brightkeel.co.uk</span>
    </div>
    <div class="contact-item contact-item--line" style="top:391px">
      <span class="contact-item__label" style="top:0">04</span>
      <span class="contact-item__value" style="top:17px">www.brightkeel.co.uk</span>
    </div>
    <div class="corner-mark"></div>
  </section>
</body>
</html>
```